Business Card Design Project

KB Consulting Associates is a management consulting business with C-suite (CEO/CFO etc) target clients. Logo selected is blue with simple/serious typefaces.

Target Market(s)

CEOs and CFOs of large corporates

Industry/Entity Type

Management Consulting

Font styles to use
Serif

Colors
3276b5

Requirements
Must have
• Tag line: Creating Meaningful Partnerships (use different font)
Address: 427 Fernvale Crescent #03-22 Singapore 519337
Telephone: +65 8372 4096
Email: kbloh@postnest42.com

```html
<!DOCTYPE html>
<html lang="en">
<head>
<meta charset="utf-8">
<title>KB Consulting Associates — Business Card</title>
<link rel="stylesheet" href="https://fonts.googleapis.com/css2?family=Crimson+Pro:wght@400;500&family=Lora:wght@400&display=swap">
<style>
  :root {
    --brand-blue: #3276b5;
    --card-white: #ffffff;
    --backdrop: #6e6e6e;
    --shadow: rgba(0, 0, 0, 0.35);
  }
  * { box-sizing: border-box; margin: 0; padding: 0; }
  html, body {
    width: 1200px;
    height: 1000px;
    overflow: hidden;
    background: var(--backdrop);
  }
  .stage {
    position: relative;
    width: 1200px;
    height: 1000px;
  }
  .card {
    position: absolute;
    width: 540px;
    height: 310px;
    background: var(--card-white);
    box-shadow: 0 12px 30px var(--shadow);
    overflow: hidden;
  }
  .card--front { left: 60px; top: 130px; }
  .card--back  { left: 600px; top: 540px; }

  /* Front */
  .brand {
    position: absolute;
    inset: 0;
    display: flex;
    align-items: center;
    justify-content: center;
    padding: 0 40px;
  }
  .brand__name {
    font-family: "Crimson Pro", serif;
    font-weight: 500;
    font-size: 38px;
    line-height: 1;
    color: var(--brand-blue);
    white-space: nowrap;
  }

  /* Back */
  .tagline-band {
    height: 152px;
    background: var(--brand-blue);
    display: flex;
    align-items: center;
    justify-content: flex-end;
    padding-right: 46px;
  }
  .tagline {
    font-family: "Lora", serif;
    font-size: 24px;
    color: var(--card-white);
    letter-spacing: 0.2px;
  }
  .contact {
    display: grid;
    grid-template-columns: auto auto;
    column-gap: 8px;
    row-gap: 0;
    justify-content: end;
    padding: 22px 96px 0 0;
    font-family: "Crimson Pro", serif;
    font-size: 19px;
    line-height: 1.3;
    color: var(--brand-blue);
  }
  .contact__label { text-align: right; font-weight: 500; }
  .contact__value { text-align: left; }
</style>
</head>
<body>
  <main class="stage">
    <section class="card card--front" aria-label="Business card front">
      <div class="brand">
        <div class="brand__name">KB Consulting Associates</div>
      </div>
    </section>

    <section class="card card--back" aria-label="Business card back">
      <div class="tagline-band">
        <p class="tagline">Creating Meaningful Partnerships</p>
      </div>
      <dl class="contact">
        <dt class="contact__label">Address:</dt>
        <dd class="contact__value">427 Fernvale Crescent #03-22</dd>
        <dt class="contact__label"></dt>
        <dd class="contact__value">Singapore 519337</dd>
        <dt class="contact__label">Telephone:</dt>
        <dd class="contact__value">+65 8372 4096</dd>
        <dt class="contact__label">Email:</dt>
        <dd class="contact__value">kbloh@postnest42.com</dd>
      </dl>
    </section>
  </main>
</body>
</html>
```